Software manual (User manual)

We need a manual for our online e-learning software. Basically what we're looking for is an Adobe InDesign setup (file) where we can add new pages and adjust textual content ourselves.

So the designer would have to come up with an elegant frontpage, page 2,3,4,5 with textual content (some lorem ipsum placeholder text) in a nice setup and a backpage.

We would like the manual to be presented in purple, specifically the purple being used in our logo (maybe cover the enitre front and backpage in purple) which is our main color (together with grey), at least for front- and back-page.

The design should be simple and elegant. Myriad-Pro Light is the font we'd like to see in headings while maybe something like Helvetica being used for the bulk text.

Industry/Entity Type

Software

Requirements
Must have
• The manual must have our logo in either colors or white depending on your choice of setup. See attached colored logo. We accept changing logo colors to all white.

It should include our email on the backpage together with the company name.

The text "User manual" should be present on the frontpage.

Either the front or backpage should have the text "edition" or "version" with a number or something similar so it's easier for users to distinguish the old manuals from the new ones.

The size should be A4

Should include an index, preferbly set up so that is updates automatically if pages are added/removed.

Each page should be numbered, aside from front and back.

As this is a user manual we do not want images. Vector graphics are ok.

"Less is more"

```html
<!DOCTYPE html>
<html lang="en">
<head>
<meta charset="utf-8">
<title>Studyra — User Manual</title>
<link href="https://fonts.googleapis.com/css2?family=Open+Sans:wght@300;700&display=swap" rel="stylesheet">
<style>
  :root {
    --purple-deep: #2d1934;
    --purple-mid: #45224f;
    --purple-bright: #5f2769;
    --white: #ffffff;
    --art-light: rgba(255,255,255,0.22);
    --art-soft: rgba(255,255,255,0.06);
  }
  * { margin: 0; padding: 0; box-sizing: border-box; }
  html, body { width: 848px; height: 1200px; overflow: hidden; }
  body { font-family: "Open Sans", Arial, sans-serif; color: var(--white); }
  .cover {
    position: relative;
    width: 848px;
    height: 1200px;
    background: linear-gradient(90deg, var(--purple-deep) 0%, var(--purple-mid) 45%, var(--purple-bright) 100%);
    overflow: hidden;
  }
  .brand-name {
    position: absolute;
    top: 170px;
    left: 0;
    width: 100%;
    text-align: center;
    font-weight: 700;
    font-size: 104px;
    letter-spacing: 1px;
    line-height: 1;
  }
  .cover-title {
    position: absolute;
    top: 392px;
    left: 0;
    width: 100%;
    text-align: center;
    font-weight: 300;
    font-size: 64px;
    letter-spacing: 1px;
    line-height: 1;
  }
  .cover-art {
    position: absolute;
    top: 560px;
    left: 60px;
    width: 730px;
    height: 370px;
    border-radius: 6px;
    background: radial-gradient(ellipse at 50% 70%, var(--art-light) 0%, var(--art-soft) 70%, transparent 100%);
  }
  .edition {
    position: absolute;
    top: 1030px;
    left: 0;
    width: 100%;
    text-align: center;
    font-weight: 300;
    font-size: 40px;
    line-height: 1;
  }
  .feature-icons {
    position: absolute;
    top: 1128px;
    left: 0;
    width: 100%;
    display: flex;
    justify-content: center;
    gap: 40px;
  }
  .feature-icons svg { width: 46px; height: 46px; display: block; }
</style>
</head>
<body>
  <main class="cover">
    <div class="brand-name">Studyra</div>
    <h1 class="cover-title">USER MANUAL</h1>
    <div class="cover-art" role="img" aria-label="Illustration of an open book with translucent squares rising from its pages"></div>
    <p class="edition">VERSION 1.0</p>
    <div class="feature-icons">
      <!-- search -->
      <svg viewBox="0 0 46 46" aria-label="Search">
        <circle cx="27" cy="18" r="12" fill="none" stroke="#fff" stroke-width="5"/>
        <line x1="18" y1="27" x2="6" y2="40" stroke="#fff" stroke-width="6" stroke-linecap="round"/>
      </svg>
      <!-- music -->
      <svg viewBox="0 0 46 46" aria-label="Audio">
        <path d="M14 8 L40 4 L40 32" fill="none" stroke="#fff" stroke-width="5"/>
        <line x1="14" y1="8" x2="14" y2="36" stroke="#fff" stroke-width="5"/>
        <ellipse cx="9" cy="37" rx="7" ry="6" fill="#fff"/>
        <ellipse cx="35" cy="33" rx="7" ry="6" fill="#fff"/>
      </svg>
      <!-- film -->
      <svg viewBox="0 0 46 46" aria-label="Video">
        <rect x="8" y="2" width="30" height="42" fill="#fff"/>
        <rect x="15" y="6" width="16" height="15" fill="#4b2455"/>
        <rect x="15" y="25" width="16" height="15" fill="#4b2455"/>
        <g fill="#4b2455">
          <rect x="10" y="6" width="3" height="4"/><rect x="10" y="14" width="3" height="4"/>
          <rect x="10" y="22" width="3" height="4"/><rect x="10" y="30" width="3" height="4"/>
          <rect x="10" y="38" width="3" height="4"/>
          <rect x="33" y="6" width="3" height="4"/><rect x="33" y="14" width="3" height="4"/>
          <rect x="33" y="22" width="3" height="4"/><rect x="33" y="30" width="3" height="4"/>
          <rect x="33" y="38" width="3" height="4"/>
        </g>
      </svg>
      <!-- info -->
      <svg viewBox="0 0 46 46" aria-label="Information">
        <circle cx="23" cy="23" r="19" fill="#fff"/>
        <circle cx="25" cy="13" r="3" fill="#522659"/>
        <path d="M19 20 H27 L24 33 H28 V35 H18 V33 H20 L22 22 H19 Z" fill="#522659"/>
      </svg>
      <!-- pie chart -->
      <svg viewBox="0 0 46 46" aria-label="Statistics">
        <path d="M23 4 A19 19 0 1 0 42 23 L23 23 Z" fill="#fff"/>
        <path d="M26 2 A18 18 0 0 1 44 20 L26 20 Z" fill="#fff"/>
      </svg>
    </div>
  </main>
</body>
</html>
```